Farhan Dalvesi Business Card

I would like an elegant business card design in both english and arabic.

Ideally a logo design with my name in Arabic (could be a tiger for example)

It should have my Name : Farhan Dalvesi
Title: Advisor / Investor
Tel. UAE +971 558 402 917
UK +44 7812 506 284
Email. farhdalv352@mailvora.com

I am an active angle investor and have many business interests in the TMT space and invest globally, the design needs to be fresh, elegant and striking.

The design should be catching and grab one's attention when they view the card.

Front card should be in English and Reverse in Arabic....

Target Market(s)

Global Investors, CEO's

Industry/Entity Type

Business

Contact Information for Business Card

Title: Advisor / Investor
Tel. UAE +971 558 402 917
UK +44 7812 506 284

Font styles to use
Serif
Other font styles liked:
• Palantino

Requirements
Must have
• A striking design with a play of my name in Arabic, could be my name that is designed as a tiger for example

```html
<!DOCTYPE html>
<html lang="en">
<head>
<meta charset="utf-8">
<title>Farhan Dalvesi Business Card</title>
<link rel="stylesheet" href="https://fonts.googleapis.com/css2?family=Arimo&family=Tinos:wght@400;700&family=Noto+Sans+Arabic:wght@400&display=swap">
<style>
  :root {
    --page: #ffffff;
    --ink: #000000;
    --card-line: #000000;
    --band-edge: #8c8c8c;
    --band-mid: #2f2f2f;
    --tiger-orange: #ff6a00;
    --tiger-dark: #1a1a1a;
  }
  html, body {
    margin: 0;
    padding: 0;
    width: 1200px;
    height: 849px;
    overflow: hidden;
    background: var(--page);
  }
  .sheet {
    position: relative;
    width: 1200px;
    height: 849px;
    color: var(--ink);
  }
  .side-label {
    position: absolute;
    font-family: "Arimo", Arial, sans-serif;
    font-size: 71px;
    line-height: 1;
    margin: 0;
    font-weight: 400;
  }
  .side-label--front { left: 155px; top: 190px; }
  .side-label--back { left: 176px; top: 582px; }

  .card {
    position: absolute;
    width: 614px;
    height: 390px;
    border: 2px solid var(--card-line);
    background: var(--page);
    overflow: hidden;
  }
  .card--front { left: 530px; top: 23px; }
  .card--back { left: 533px; top: 432px; }

  .card__name {
    position: absolute;
    top: 26px;
    left: 37px;
    margin: 0;
    font-family: "Tinos", "Times New Roman", serif;
    font-size: 46px;
    font-weight: 400;
    line-height: 1;
    letter-spacing: -0.5px;
  }
  .card__name-ar {
    position: absolute;
    top: 28px;
    left: 338px;
    width: 200px;
    text-align: center;
    font-family: "Noto Sans Arabic", Arial, sans-serif;
    font-size: 34px;
    line-height: 1.1;
  }
  .card__band {
    position: absolute;
    left: 0;
    top: 106px;
    width: 100%;
    height: 164px;
    background: linear-gradient(to bottom, var(--band-edge) 0%, var(--band-mid) 50%, var(--band-edge) 100%);
  }
  .card__emblem {
    position: absolute;
    left: 141px;
    top: 6px;
    width: 350px;
    height: 158px;
  }

  .contact-ar {
    position: absolute;
    top: 284px;
    left: 10px;
    width: 352px;
    text-align: center;
    font-family: "Noto Sans Arabic", Arial, sans-serif;
    font-size: 12px;
    line-height: 30px;
  }
  .contact-ar p { margin: 0; }
  .contact-ar .contact-ar__line--large { font-size: 15px; }
  .title-ar {
    position: absolute;
    top: 322px;
    right: 34px;
    margin: 0;
    font-family: "Noto Sans Arabic", Arial, sans-serif;
    font-size: 15px;
  }

  .title-en {
    position: absolute;
    left: 23px;
    top: 318px;
    margin: 0;
    font-family: "Tinos", "Times New Roman", serif;
    font-weight: 700;
    font-size: 17px;
  }
  .contact-en {
    position: absolute;
    left: 278px;
    top: 284px;
    margin: 0;
    font-family: "Tinos", "Times New Roman", serif;
    font-size: 16.5px;
    line-height: 31px;
  }
  .contact-en p { margin: 0; }
  .contact-en .contact-en__indent { padding-left: 5px; }
</style>
</head>
<body>
<main class="sheet">
  <h2 class="side-label side-label--front">Front</h2>
  <h2 class="side-label side-label--back">Back</h2>

  <section class="card card--front" aria-label="Card front">
    <h1 class="card__name">Farhan Dalvesi</h1>
    <div class="card__name-ar" lang="ar" dir="rtl">فرحان دالفيسي</div>
    <div class="card__band">
      <svg class="card__emblem" viewBox="0 0 350 158" role="img" aria-label="Leaping tiger emblem formed from the name in Arabic lettering">
        <defs>
          <linearGradient id="tigerFront" x1="0" y1="0" x2="1" y2="1">
            <stop offset="0" stop-color="var(--tiger-orange)"/>
            <stop offset="0.7" stop-color="var(--tiger-orange)"/>
            <stop offset="1" stop-color="var(--tiger-dark)"/>
          </linearGradient>
        </defs>
        <rect x="0" y="0" width="350" height="158" rx="40" fill="url(#tigerFront)"/>
      </svg>
    </div>
    <div class="contact-ar" lang="ar" dir="rtl">
      <p>البريد الإلكتروني. <span dir="ltr">farhdalv352@mailvora.com</span></p>
      <p>الهاتف . الإمارات العربية المتحدة <span dir="ltr">+971 558 402 917</span></p>
      <p class="contact-ar__line--large">المملكة المتحدة <span dir="ltr">+44 7812 506 284</span></p>
    </div>
    <p class="title-ar" lang="ar" dir="rtl">العنوان: المستشار / المستثمر</p>
  </section>

  <section class="card card--back" aria-label="Card back">
    <h1 class="card__name">Farhan Dalvesi</h1>
    <div class="card__name-ar" lang="ar" dir="rtl">فرحان دالفيسي</div>
    <div class="card__band">
      <svg class="card__emblem" viewBox="0 0 350 158" role="img" aria-label="Leaping tiger emblem formed from the name in Arabic lettering">
        <defs>
          <linearGradient id="tigerBack" x1="0" y1="0" x2="1" y2="1">
            <stop offset="0" stop-color="var(--tiger-orange)"/>
            <stop offset="0.7" stop-color="var(--tiger-orange)"/>
            <stop offset="1" stop-color="var(--tiger-dark)"/>
          </linearGradient>
        </defs>
        <rect x="0" y="0" width="350" height="158" rx="40" fill="url(#tigerBack)"/>
      </svg>
    </div>
    <p class="title-en">Title: Advisor / Investor</p>
    <div class="contact-en">
      <p>Email. farhdalv352@mailvora.com</p>
      <p>Tel. UAE +971 558 402 917</p>
      <p class="contact-en__indent">UK +44 7812 506 284</p>
    </div>
  </section>
</main>
</body>
</html>
```